Natural Cosmetics need a Packaging Design

We need a PACKAGING design for labels on hand/body wash bottles and soap paper boxes.
We target at high end markets.
We expect a contemporary and trendy design.
We don't need a separate logo. The brand name "Va Mirel" acts as the logo.
We want a modern and classic font for "Va Mirel".
Please see attached pictures for packaging samples.

Industry/Entity Type

Cosmetics

Requirements
Should not have
• a separate logo from the brand name

```html
<!DOCTYPE html>
<html lang="en">
<head>
<meta charset="UTF-8">
<title>Va Mirel Hands &amp; Body Wash Label</title>
<link href="https://fonts.googleapis.com/css2?family=Josefin+Sans:wght@300;400;600&display=swap" rel="stylesheet">
<style>
  :root {
    --canvas: #ffffff;
    --purple-deep: #4f1a86;
    --purple-mid: #6a2aa6;
    --teal-dark: #23818a;
    --teal-mid: #4fb1b8;
    --teal-light: #c4f0f1;
    --white: #ffffff;
  }
  html, body {
    margin: 0;
    padding: 0;
    width: 1200px;
    height: 1200px;
    overflow: hidden;
    background: var(--canvas);
    font-family: "Josefin Sans", sans-serif;
  }
  .canvas {
    position: relative;
    width: 1200px;
    height: 1200px;
  }
  .label {
    position: absolute;
    left: 220px;
    top: 90px;
    width: 760px;
    height: 1040px;
    border-radius: 14px;
    overflow: hidden;
  }
  .label-artwork {
    position: absolute;
    inset: 0;
    background: linear-gradient(180deg, var(--teal-mid) 0%, var(--teal-dark) 20%, var(--teal-mid) 55%, var(--teal-light) 100%);
  }
  .brand-name {
    position: absolute;
    left: 0;
    top: 40px;
    width: 100%;
    margin: 0;
    text-align: center;
    color: var(--white);
    font-weight: 600;
    font-size: 84px;
    line-height: 100px;
    letter-spacing: 1px;
  }
  .product-title {
    position: absolute;
    left: 100px;
    top: 500px;
    margin: 0;
    font-weight: 300;
    font-size: 150px;
    line-height: 118px;
    text-transform: uppercase;
  }
  .product-title span { display: block; }
  .title-hands { color: var(--white); }
  .title-body { padding-left: 95px; color: var(--white); }
  .title-wash { padding-left: 80px; color: var(--purple-deep); }
  .benefit {
    position: absolute;
    left: 280px;
    top: 910px;
    margin: 0;
    color: var(--purple-deep);
    font-weight: 400;
    font-size: 46px;
  }
  .ingredient-band {
    position: absolute;
    left: 0;
    bottom: 0;
    width: 100%;
    height: 62px;
    background: var(--purple-mid);
    color: var(--white);
    font-size: 40px;
    font-weight: 400;
    display: flex;
    align-items: center;
    justify-content: center;
  }
</style>
</head>
<body>
<main class="canvas">
  <section class="label">
    <div class="label-artwork" role="img" aria-label="Underwater photograph of clear teal water with rising air bubbles"></div>

    <p class="brand-name">Va Mirel</p>

    <h1 class="product-title">
      <span class="title-hands">Hands&amp;</span>
      <span class="title-body">Body</span>
      <span class="title-wash">Wash</span>
    </h1>

    <p class="benefit">moisture</p>
    <div class="ingredient-band">with vitamin e</div>
  </section>
</main>
</body>
</html>
```